Flyer für dynamisches Maklerteam
The design process with Brightwing went very well. He responded precisely to our requirements and to our target group and developed designs that reflect our logo and our corporate identity in many small details. Communication with Brightwing went great. He quickly translated our requests into wonderful designs and created flyers that we are very happy with. Brightwing is a good designer and I can highly recommend working with him. Dr. Ilse Brandvoort KORVEN Real Estate
Zielgruppe
KORVEN Immobilien ist ein dynamisches Maklerteam, dass sich auf den Verkauf von Wohnimmobilien des gehobenen Preissegmentes spezialisiert hat. Unser Schwerpunkt liegt auf Luxusobjekten.
Hallo,
schön, dass ihr an unserem Design-Wettbewerb teilnehmt.
Unser Zielgruppe sind verkaufswillige Eigentümer hochpreisiger Immobilien.
--> eine ganz wichtige Kundengruppe sind Erben, die ihre geerbte Immobilie verkaufen wollen.
Wir wünschen uns beidseitig bedruckte Flyer auf hochwertigem Material (Chromosulfatpapier, 450 g/m²). Bei der Auswahl des Formates wollen wir euch freie Hand lassen.
Vorderseite:
- Logo von KORVEN Immobilien.
- Ein Foto als Eye-Catcher, das Interesse weckt, zum Schmunzeln bringt und in Erinnerung bleibt. Wichtig: Auf dem Foto sollte man Freude sehen (gerne lächelnde Gesichter, die Personen müssen nicht zwangsläufig in die Kamera blicken. Eine positive und glückliche Grundstimmung auf dem Bild ist wichtig). -> an dieser Stelle bitte geeignete Stock-Bilder recherchieren und diese vorschlagen.
- Claim: Genießen Sie Ihre Freiheit. Wir verkaufen Ihre Immobilie.
Rückseite:
folgenden Text bitte verwenden:
Das Besondere bei KORVEN Immobilien:
- langjährige Erfahrung mit Immobilien des gehobenen Segments
- hochprofessionelle Komplettabwicklung in kürzester Zeit
- ausgezeichnete Referenzen
- auf Wunsch sehr diskrete Abwicklung
Anschließend bitte einen Satz, der eine Abschlussfrage formuliert, die etwa folgenden Inhalt wiedergibt:
'Wenn Sie direkt mit uns sprechen möchten, erreichen Sie uns jederzeit unter 0157 - 3948 2036.'
(Diesen Satz könnt ihr gerne umformulieren.)
Website und Emailadresse [ www.korven-immobilien.example - ib@korven-immobilien.example ]
Bilder des gesamten KORVEN Verkaufsteam als Einzelportraits vor dunklem Hintergrund.
Dabei wichtig: Lorenz Korven als Chef bitte an die erste Stelle setzen. Henrike und Jonas Weidlich sind ein Ehepaar, die Immobilien meist gemeinsam verkaufen, daher bitte auch ihre beiden Portraits nebeneinander platzieren.
Bei der Gestaltung des Flyers i..

```html
<!DOCTYPE html>
<html lang="de">
<head>
<meta charset="utf-8">
<title>KORVEN Immobilien – Flyer</title>
<link href="https://fonts.googleapis.com/css2?family=Josefin+Sans:wght@300;400&family=Tenor+Sans&display=swap" rel="stylesheet">
<style>
  :root {
    --navy: #1b2170;
    --navy-deep: #141a5c;
    --paper: #e6e6e8;
    --backdrop: #d6cec8;
    --white: #ffffff;
  }
  * { box-sizing: border-box; margin: 0; padding: 0; }
  html, body { width: 1200px; height: 900px; overflow: hidden; }
  body {
    background: var(--backdrop);
    font-family: "Josefin Sans", sans-serif;
    position: relative;
  }
  .sc { font-size: 0.78em; text-transform: uppercase; }
  .flyer {
    position: absolute;
    left: 220px;
    width: 760px;
    height: 405px;
    overflow: hidden;
    background: var(--navy);
    box-shadow: 0 6px 18px rgba(40, 30, 30, 0.18);
  }
  .flyer--front { top: 30px; }
  .flyer--back { top: 465px; }

  /* Front */
  .hero-photo {
    position: absolute;
    inset: 0;
    background: linear-gradient(100deg, #5d6670 0%, #b9c2cb 30%, #e9ecef 48%, #7f96b5 62%, #8fa6c4 78%, #4e5a6a 100%);
    clip-path: polygon(295px 0, 760px 0, 760px 405px, 201px 405px);
  }
  .brand {
    position: absolute;
    color: var(--white);
    text-align: center;
  }
  .brand__name {
    font-family: "Tenor Sans", sans-serif;
    font-size: 46px;
    letter-spacing: 5px;
    line-height: 1;
    display: block;
  }
  .brand__rule {
    display: block;
    height: 1px;
    background: var(--white);
    margin: 8px auto 6px;
    width: 100%;
  }
  .brand__sub {
    font-family: "Tenor Sans", sans-serif;
    font-size: 12px;
    letter-spacing: 9px;
    display: block;
  }
  .flyer--front .brand { left: 28px; top: 106px; width: 220px; }
  .claim-box {
    position: absolute;
    left: 0;
    top: 255px;
    width: 368px;
    height: 117px;
    background: var(--paper);
    padding: 28px 0 0 20px;
    color: var(--navy);
    font-size: 24px;
    font-weight: 300;
    line-height: 33px;
  }

  /* Back */
  .flyer--back .brand { left: 46px; top: 30px; width: 190px; }
  .flyer--back .brand__name { font-size: 40px; letter-spacing: 4px; }
  .flyer--back .brand__sub { font-size: 11px; letter-spacing: 8px; }
  .usp-list {
    position: absolute;
    left: 318px;
    top: 44px;
    list-style: none;
    color: var(--white);
    font-size: 12px;
    line-height: 18px;
  }
  .usp-list li::before {
    content: "";
    display: inline-block;
    width: 5px; height: 5px;
    background: var(--white);
    margin-right: 5px;
    vertical-align: 2px;
  }
  .contact-band {
    position: absolute;
    left: 0; top: 256px;
    width: 760px; height: 115px;
    background: var(--paper);
  }
  .team {
    position: absolute;
    top: 136px;
    left: 0;
    width: 760px;
    height: 140px;
  }
  .portrait {
    position: absolute;
    top: 0;
    width: 108px;
    height: 139px;
    background: radial-gradient(ellipse at 50% 40%, #4a4a50 0%, #1e1e22 70%);
    border-bottom: 4px solid var(--navy);
  }
  .closing {
    position: absolute;
    left: 28px;
    top: 306px;
    color: var(--navy);
    font-size: 15px;
    line-height: 23px;
  }
  .reach {
    position: absolute;
    right: 22px;
    top: 282px;
    color: var(--navy);
    text-align: right;
  }
  .reach__phone {
    font-size: 36px;
    font-weight: 300;
    line-height: 40px;
    display: flex;
    align-items: center;
    justify-content: flex-end;
    gap: 6px;
  }
  .reach__phone svg { width: 20px; height: 20px; }
  .reach__web {
    font-size: 18px;
    font-weight: 300;
    letter-spacing: 0.5px;
    line-height: 22px;
  }
  .reach__mail {
    font-size: 14px;
    font-weight: 300;
    letter-spacing: 0.5px;
    line-height: 18px;
  }
</style>
</head>
<body>

<section class="flyer flyer--front" aria-label="Flyer Vorderseite">
  <div class="hero-photo" role="img" aria-label="Foto: lächelndes Paar in hellblauen Hemden spaziert Hand in Hand vor einer modernen Villa"></div>
  <div class="brand">
    <span class="brand__name">KORVEN</span>
    <span class="brand__rule"></span>
    <span class="brand__sub">IMMOBILIEN</span>
  </div>
  <p class="claim-box">G<span class="sc">enie</span>ß<span class="sc">en</span> S<span class="sc">ie</span> I<span class="sc">hre</span> F<span class="sc">reiheit</span>.<br>W<span class="sc">ir verkaufen</span> I<span class="sc">hre</span> I<span class="sc">mmobilie</span>.</p>
</section>

<section class="flyer flyer--back" aria-label="Flyer Rückseite">
  <div class="brand">
    <span class="brand__name">KORVEN</span>
    <span class="brand__rule"></span>
    <span class="brand__sub">IMMOBILIEN</span>
  </div>
  <ul class="usp-list">
    <li>L<span class="sc">angjährige</span> E<span class="sc">rfahrung mit</span> I<span class="sc">mmobilien des gehobenen</span> S<span class="sc">egments</span></li>
    <li>H<span class="sc">ochprofessionelle</span> K<span class="sc">omplettabwicklung in kürzester</span> Z<span class="sc">eit</span></li>
    <li>A<span class="sc">usgezeichnete</span> R<span class="sc">eferenzen</span></li>
    <li>A<span class="sc">uf</span> W<span class="sc">unsch sehr diskrete</span> A<span class="sc">bwicklung</span></li>
  </ul>
  <div class="contact-band"></div>
  <div class="team">
    <div class="portrait" style="left:22px" role="img" aria-label="Portrait Lorenz Korven vor dunklem Hintergrund"></div>
    <div class="portrait" style="left:144px" role="img" aria-label="Portrait Teammitglied vor dunklem Hintergrund"></div>
    <div class="portrait" style="left:266px" role="img" aria-label="Portrait Teammitglied vor dunklem Hintergrund"></div>
    <div class="portrait" style="left:388px" role="img" aria-label="Portrait Teammitglied vor dunklem Hintergrund"></div>
    <div class="portrait" style="left:510px" role="img" aria-label="Portrait Teammitglied vor dunklem Hintergrund"></div>
    <div class="portrait" style="left:632px" role="img" aria-label="Portrait Teammitglied vor dunklem Hintergrund"></div>
  </div>
  <p class="closing">W<span class="sc">enn</span> S<span class="sc">ie direkt mit uns sprechen möchten</span>,<br><span class="sc">erreichen</span> S<span class="sc">ie uns jederzeit unter</span></p>
  <div class="reach">
    <div class="reach__phone">
      <svg viewBox="0 0 20 20" aria-hidden="true">
        <circle cx="10" cy="10" r="10" fill="#1b2170"/>
        <path d="M7 5c1 0 1.6 1.8 1.4 2.4-.2.6-.9.8-.7 1.5.3 1 1.3 2.2 2.4 2.6.6.2.9-.5 1.5-.6.7-.1 2.3.7 2.2 1.6-.1 1-1.5 1.8-2.5 1.6C8.6 13.6 6 10.8 5.7 7.8 5.6 6.4 6.2 5 7 5z" fill="#e6e6e8"/>
      </svg>
      <span>0157 – 3948 2036</span>
    </div>
    <div class="reach__web">WWW.KORVEN-IMMOBILIEN.EXAMPLE</div>
    <div class="reach__mail">IB@KORVEN-IMMOBILIEN.EXAMPLE</div>
  </div>
</section>

</body>
</html>
```